Business Card Design Project

We are a tiling/bathroom renovation business based in Brisbane Australia and are looking to get a professional looking business card designed to promote ourselves.

We provide quality workmanship to upgrade/enhance peoples' homes.
Updates

Target Market(s)

Homeowners looking to renovate their bathrooms, or get tiling done. Mostly young adults to elderly who can spare several grand to upgrade their home

Industry/Entity Type

Business

Requirements
Must have
• A bold heading is a must: "Tiling Corvel & Dray"
Must include these details: "ABN: 41 938 106 274", "BSA Licence: 8073162", "Bastien: 0491 873 210", "Rhys: 0468 215 093", "Email: tilingcorvelanddray@quillmarsh.com", "Let Us Set It Straight".

An abstract geometrical logo that's based around squares and straight lines/arrows because we are a tiling business and our slogan is "Let Us Set It Straight"
Nice to have
• I have attached an image of a logo design I got from markvesta.com, and the background from Cardlorne.com.au templates I really like together I just need the cut and paste look ironed out.

You are free to play around with different looks and feels but around the same theme as my sample. i.e. simple but striking, minimal but eye catching, or not maybe something unexpected could be perfect who knows?
Should not have
• Photorealism on a business card is a pet peeve. Too much detail for a teeny tiny business card. A Business card should stand out at a distance and you shouldn't have to squint to see it's detail.

```html
<!DOCTYPE html>
<html lang="en">
<head>
<meta charset="utf-8">
<title>Tiling Corvel &amp; Dray – Business Card</title>
<link rel="stylesheet" href="https://fonts.googleapis.com/css2?family=Arimo:wght@400;700&family=Cormorant+Upright:wght@500&display=swap">
<style>
  :root {
    --page-bg: #ffffff;
    --card-light-left: #a9d2f7;
    --card-mid: #3a86dc;
    --card-deep: #0b4fa6;
    --card-light-right: #6ec6f6;
    --text-light: #ffffff;
    --text-dark: #0a0a0a;
  }
  * { margin: 0; padding: 0; box-sizing: border-box; }
  html, body {
    width: 1200px;
    height: 673px;
    overflow: hidden;
    background: var(--page-bg);
  }
  .canvas {
    position: relative;
    width: 1200px;
    height: 673px;
  }
  .card {
    position: absolute;
    left: 182px;
    top: 82px;
    width: 838px;
    height: 488px;
    overflow: hidden;
  }
  .card-backdrop {
    position: absolute;
    inset: 0;
    background:
      linear-gradient(180deg, rgba(255,255,255,0.12) 0%, rgba(255,255,255,0) 45%),
      linear-gradient(90deg,
        var(--card-light-left) 0%,
        var(--card-mid) 22%,
        var(--card-deep) 38%,
        var(--card-mid) 62%,
        var(--card-light-right) 100%);
  }
  .card-content {
    position: absolute;
    inset: 0;
  }
  .brand {
    position: absolute;
    left: 0;
    right: 0;
    top: 52px;
    display: flex;
    justify-content: center;
    align-items: center;
    gap: 22px;
    color: var(--text-light);
    font-family: "Arimo", Arial, sans-serif;
    font-weight: 700;
    font-size: 62px;
    line-height: 1;
    white-space: nowrap;
  }
  .brand-square {
    width: 46px;
    height: 46px;
    background: var(--text-light);
    flex: none;
  }
  .tagline {
    position: absolute;
    left: 0;
    right: 0;
    top: 176px;
    text-align: center;
    color: var(--text-light);
    font-family: "Cormorant Upright", serif;
    font-weight: 500;
    font-size: 82px;
    line-height: 1;
  }
  .registration,
  .contact {
    position: absolute;
    color: var(--text-dark);
    font-family: "Arimo", Arial, sans-serif;
    line-height: 1;
    white-space: nowrap;
  }
  .registration {
    top: 279px;
    font-size: 20px;
    font-weight: 400;
  }
  .registration-abn { left: 113px; }
  .registration-licence { left: 502px; }
  .contact {
    font-weight: 700;
  }
  .contact-phone {
    top: 373px;
    font-size: 29px;
  }
  .contact-bastien { left: 58px; }
  .contact-rhys { left: 502px; }
  .contact-email {
    left: 0;
    right: 0;
    top: 432px;
    text-align: center;
    font-size: 25px;
  }
</style>
</head>
<body>
  <div class="canvas">
    <section class="card" aria-label="Tiling Corvel &amp; Dray business card">
      <div class="card-backdrop" role="img" aria-label="Blue background of tiles receding in perspective"></div>
      <div class="card-content">
        <h1 class="brand"><span class="brand-square" aria-hidden="true"></span><span class="brand-name">Tiling Corvel &amp; Dray</span></h1>
        <p class="tagline">Let us set it straight</p>
        <p class="registration registration-abn">ABN: 41 938 106 274</p>
        <p class="registration registration-licence">BSA Licence: 8073162</p>
        <p class="contact contact-phone contact-bastien">Bastien: 0491 873 210</p>
        <p class="contact contact-phone contact-rhys">Rhys: 0468 215 093</p>
        <p class="contact contact-email">Email: tilingcorvelanddray@quillmarsh.com</p>
      </div>
    </section>
  </div>
</body>
</html>
```